I would like to update my one-page service sheet to provide a more professional/polished look and...

One page service sheet - with content on both the front and back. I've uploaded my current one page service sheet to provide background. I've also included a service sheet that I recently received from another business owner (from a very different business) that is a representation of the kind of feel I'm looking for. My business website may be found at: www.torvilunconsulting.com

```html
<!DOCTYPE html>
<html lang="en">
<head>
<meta charset="utf-8">
<title>Torvilun Consulting – Service Sheet</title>
<link href="https://fonts.googleapis.com/css2?family=Montserrat:wght@400;600;700;800;900&family=Open+Sans:ital,wght@1,400&display=swap" rel="stylesheet">
<style>
:root{
  --orange:#e8731f;
  --slate:#3b4553;
  --ink:#2b2f36;
  --paper:#ffffff;
  --stage:#3a3b3d;
}
*{box-sizing:border-box;margin:0;padding:0}
html,body{width:1200px;height:776px;overflow:hidden;background:var(--stage);font-family:"Montserrat",sans-serif}
.sheet{position:absolute;top:38px;width:540px;height:700px;background:var(--paper);overflow:hidden}
.sheet--front{left:50px}
.sheet--back{left:610px}
.hero{position:absolute;left:0;top:0;width:540px;height:212px;
  background:linear-gradient(100deg,#3a2418 0%,#7a3e1e 30%,#c0622a 60%,#d9823e 80%,#8a4a24 100%)}
.hero__headline{position:absolute;left:80px;top:78px;width:380px;text-align:center;color:#fff;font-weight:600;font-size:21px;line-height:1.3}
.hero__rule{position:absolute;left:200px;top:146px;width:140px;height:2px;background:#fff}
.banner{position:absolute;background:var(--slate);overflow:hidden}
.banner__photo{position:absolute;top:0;right:0;bottom:0}
.banner__title{position:absolute;left:18px;color:var(--orange);font-weight:900;font-size:24px;line-height:1;text-transform:uppercase;letter-spacing:.3px}
.banner__lede{position:absolute;left:18px;color:#fff;font-weight:600;font-size:11.5px;line-height:1.3}
.services{position:absolute;display:flex;gap:4px}
.service{flex:1}
.service__bar{height:8px;background:var(--slate);margin-bottom:8px}
.service--accent .service__bar{background:var(--orange)}
.service__text{font-size:8.6px;line-height:1.35;color:var(--ink);padding-right:4px}
.service__text b{font-weight:700}
.service--accent .service__text{color:var(--orange)}
.quote{position:absolute;left:60px;top:530px;width:420px;height:78px;border:3px solid var(--slate);text-align:center;padding:10px 18px 0}
.quote__text{font-family:"Open Sans",sans-serif;font-style:italic;font-size:14px;line-height:1.3;color:var(--ink)}
.quote__cite{display:block;color:var(--orange);font-weight:700;font-size:10px;margin-top:3px;font-style:normal}
.contact-band{position:absolute;left:0;background:var(--orange);color:#fff;font-weight:700;font-size:10.5px;line-height:1.4;padding:10px 0 0 34px}
.brand-block{position:absolute;background:var(--paper);display:flex;align-items:center;gap:8px;padding-left:12px}
.brand-block__mark{width:11px;height:11px;background:var(--orange);flex:none}
.brand-block__name{color:var(--slate);font-weight:800;font-size:13.5px;line-height:1.15;letter-spacing:.3px;white-space:nowrap}
.corner-square{position:absolute;right:0;background:var(--slate)}
</style>
</head>
<body>

<section class="sheet sheet--front">
  <div class="hero" role="img" aria-label="Photo of a climber helping another up a cliff at sunset"></div>
  <p class="hero__headline">Replace confusion and hesitation with clarity and resolve.</p>
  <div class="hero__rule"></div>

  <div class="banner" style="left:32px;top:232px;width:476px;height:160px">
    <div class="banner__photo" role="img" aria-label="Photo of hikers climbing a ridge above the clouds at sunrise" style="width:330px;background:linear-gradient(90deg,var(--slate) 0%,#6a5a4e 25%,#d38a4a 55%,#e8a45e 75%,#b8733e 100%)"></div>
    <h2 class="banner__title" style="top:20px">Growth<br>Strategy &amp;<br>Innovation</h2>
    <p class="banner__lede" style="top:98px;width:130px">Discover what's needed to reach the next stage of growth.</p>
  </div>

  <div class="services" style="left:32px;top:392px;width:476px">
    <div class="service"><div class="service__bar"></div><p class="service__text"><b>Growth Strategy &amp; Business Model Review.</b> Gain an objective perspective on your growth strategy and business.</p></div>
    <div class="service service--accent"><div class="service__bar"></div><p class="service__text"><b>Revenue Acceleration &amp; Lead Generation.</b> Define and execute strategies and tactics to drive demand and top line growth.</p></div>
    <div class="service"><div class="service__bar"></div><p class="service__text"><b>Execution and Scale.</b> Enable your people, processes, and technology to meet the demands of growth.</p></div>
    <div class="service service--accent"><div class="service__bar"></div><p class="service__text"><b>Pricing Strategies.</b> Strategically price products and services.</p></div>
    <div class="service"><div class="service__bar"></div><p class="service__text"><b>Growth Training.</b> Group and individual training/ coaching.</p></div>
  </div>

  <blockquote class="quote">
    <p class="quote__text">"We are what we repeatedly do. Excellence, therefore, is not an act, but a habit."</p>
    <cite class="quote__cite">OLD PROVERB</cite>
  </blockquote>

  <div class="corner-square" style="top:590px;width:70px;height:62px"></div>
  <div class="contact-band" style="top:626px;width:330px;height:60px">
    Dana Hollerin | 555.014.2783<br>admin@torvilunconsulting.com<br>www.torvilunconsulting.com
  </div>
  <div class="brand-block" style="left:318px;top:600px;width:150px;height:56px">
    <span class="brand-block__mark"></span>
    <span class="brand-block__name">TORVILUN<br>CONSULTING</span>
  </div>
</section>

<section class="sheet sheet--back">
  <div class="banner" style="left:30px;top:24px;width:466px;height:160px">
    <div class="banner__photo" role="img" aria-label="Photo of aerobatic jets flying in formation across a blue sky" style="width:300px;background:linear-gradient(90deg,var(--slate) 0%,#4f6a8c 30%,#7fa3cc 65%,#a8c4e2 100%)"></div>
    <h2 class="banner__title" style="top:18px">Growth<br>Process &amp;<br>Execution</h2>
    <p class="banner__lede" style="top:94px;width:170px;font-size:10.5px">Fine-tune and formalize growth processes for efficiency, effectiveness, and scale.</p>
  </div>

  <div class="services" style="left:30px;top:184px;width:466px">
    <div class="service service--accent"><div class="service__bar" style="background:var(--slate)"></div><p class="service__text"><b>Innovation Capture &amp; Elaboration.</b> Standardize ideacapture, analysis, funding, elaboration, and innovation roll-out.</p></div>
    <div class="service"><div class="service__bar" style="background:var(--orange)"></div><p class="service__text"><b>Growth Channel Optimization.</b> Enhance the prospect and customer experience by blending digital and traditional.</p></div>
    <div class="service service--accent"><div class="service__bar" style="background:var(--slate)"></div><p class="service__text"><b>Business Development.</b> Transform business development into a proactive "team sport" and increase accountability.</p></div>
    <div class="service"><div class="service__bar" style="background:var(--orange)"></div><p class="service__text"><b>Prospect &amp; Client Experience Mapping.</b> Create greater client stickiness, brand resonance, and be "easier to do business with."</p></div>
  </div>

  <div class="banner" style="left:56px;top:300px;width:460px;height:150px">
    <div class="banner__photo" role="img" aria-label="Illustration of glowing digital business icons over a dark blue background" style="width:290px;background:linear-gradient(90deg,var(--slate) 0%,#2c4a72 35%,#3d6fa8 65%,#1f3556 100%)"></div>
    <h2 class="banner__title" style="top:20px">Growth<br>Solutions &amp;<br>Analytics</h2>
    <p class="banner__lede" style="top:100px;width:170px">Get the right capabilities in place to support your growth journey.</p>
  </div>

  <div class="services" style="left:56px;top:450px;width:460px">
    <div class="service"><div class="service__bar" style="background:var(--orange)"></div><p class="service__text"><b>Technology Strategy &amp; Roadmap.</b> Ensure that the right technology is in place for each step of your growth journey.</p></div>
    <div class="service service--accent"><div class="service__bar" style="background:var(--slate)"></div><p class="service__text"><b>Software Selection.</b> Identify the specific capabilities and vendors that are most appropriate for your business.</p></div>
    <div class="service"><div class="service__bar" style="background:var(--orange)"></div><p class="service__text"><b>Project Leadership.</b> Get critical projects over the finish line.</p></div>
    <div class="service service--accent"><div class="service__bar" style="background:var(--slate)"></div><p class="service__text"><b>Disruptive Trends.</b> Demystify "Digital," "Big Data," "Artificial Intelligence," and "Internet of Things" to create advantage.</p></div>
    <div class="service"><div class="service__bar" style="background:var(--orange)"></div><p class="service__text"><b>Critical Metrics.</b> Determine the leading and lagging metrics that are most critical for your business.</p></div>
  </div>

  <div class="corner-square" style="top:574px;width:66px;height:62px"></div>
  <div class="contact-band" style="top:602px;width:330px;height:62px">
    Dana Hollerin | 555.014.2783<br>dhollerin@torvilunconsulting.com<br>www.torvilunconsulting.com
  </div>
  <div class="brand-block" style="left:320px;top:580px;width:152px;height:56px">
    <span class="brand-block__mark"></span>
    <span class="brand-block__name">TORVILUN<br>CONSULTING</span>
  </div>
</section>

</body>
</html>
```